NEED Homepage Website Design for Event Planning Business

We need a homepage mockup for an event planning company based in Massachusetts. We provide a custom trailer to rent along with chairs, tables, lighting, etc.

Please add a "Check Availability" call to action which is just a form
- First & Last Name
- Phone
- Email Address
- Date Request

Add an Instagram section (use attached photos as we do not even have an IG account yet)

1 page

```html
<!DOCTYPE html>
<html lang="en">
<head>
<meta charset="utf-8">
<title>Hearthside Events</title>
<link href="https://fonts.googleapis.com/css2?family=Figtree:wght@400;500;600;700&display=swap" rel="stylesheet">
<style>
:root{
  --orange:#f47216;
  --orange-dark:#d85e0a;
  --ink:#1f1f1f;
  --text:#3a3a3a;
  --muted:#555;
  --light:#f4f4f4;
  --dark:#231f20;
  --line:#d7d7d7;
  --white:#fff;
}
*{margin:0;padding:0;box-sizing:border-box}
html,body{width:1200px;height:2555px;overflow:hidden}
body{font-family:"Figtree",sans-serif;color:var(--text);background:var(--white);position:relative}
.abs{position:absolute}
.btn{position:absolute;background:linear-gradient(var(--orange),var(--orange-dark));color:var(--white);font-weight:600;font-size:10px;border-radius:14px;display:flex;align-items:center;justify-content:center}
.brand{position:absolute;font-weight:700;color:var(--ink);display:flex;align-items:center;gap:8px}
.brand .dot{width:12px;height:12px;background:var(--orange);border-radius:50%}
/* header */
.nav{position:absolute;top:24px;left:439px;display:flex;gap:24px;font-size:10.5px;font-weight:600;color:var(--ink)}
.nav .active{color:var(--orange)}
.phone{position:absolute;left:771px;top:23px;color:var(--orange);font-size:11.5px;font-weight:500;display:flex;gap:6px;align-items:center}
/* hero */
.hero{position:absolute;top:62px;left:0;width:1200px;height:438px;background:linear-gradient(135deg,#4b5a52,#6c6f62 40%,#54483d 70%,#3d4340)}
.hero-copy{position:absolute;top:210px;width:1200px;text-align:center;color:var(--white)}
.hero-copy h3{font-size:19px;font-weight:600}
.hero-copy h1{font-size:31px;font-weight:700;line-height:36px;margin-top:4px}
/* about */
.about{position:absolute;top:500px;left:0;width:1200px;height:293px;background:var(--light)}
.section-title{font-size:31px;font-weight:600;color:var(--ink);display:flex;align-items:center;gap:14px}
.section-title .bar{display:inline-block;width:62px;height:1.5px;background:var(--ink)}
.about p{font-size:10.5px;line-height:15px;color:var(--muted)}
.frame{position:absolute;left:794px;top:563px;width:206px;height:229px;border:2px solid var(--ink)}
.card{position:absolute;left:769px;top:588px;width:206px;height:230px;background:var(--orange);padding:16px 19px}
.card h4{color:var(--white);font-size:16px;font-weight:600;text-align:center;margin-bottom:14px}
.field{background:var(--white);height:24px;border-radius:2px;font-size:8.5px;color:var(--ink);padding:0 9px;display:flex;align-items:center;justify-content:space-between;margin-bottom:7.5px}
.card .submit{background:var(--ink);color:var(--white);height:25px;border-radius:2px;font-size:9.5px;font-weight:600;display:flex;align-items:center;justify-content:center}
/* services */
.acc{position:absolute;left:200px;width:800px;height:38px;border-bottom:1px solid var(--line);display:flex;align-items:center;justify-content:space-between;padding:0 24px;font-size:14px;font-weight:500;color:var(--ink)}
.acc.open{background:linear-gradient(var(--orange),var(--orange-dark));color:var(--white);border:none}
.plus{width:11px;height:11px;border:1px solid var(--orange);border-radius:50%;position:relative}
.plus:before,.plus:after{content:"";position:absolute;background:var(--orange);left:2px;top:4px;width:5px;height:1px}
.plus:after{left:4px;top:2px;width:1px;height:5px}
.open .plus{border-color:var(--white)}
.open .plus:before{background:var(--white)}
.open .plus:after{display:none}
.tent-text{position:absolute;left:612px;top:1120px;width:388px;font-size:10.5px;line-height:15px;color:var(--muted)}
.tent-text h3{color:var(--orange);font-size:19px;font-weight:600;margin-bottom:16px}
.tent-text b{color:var(--ink)}
.tent-text ul{list-style:none;margin-top:16px}
.tent-text li{position:relative;padding-left:28px;margin-bottom:15px}
.tent-text li svg{position:absolute;left:0;top:-2px}
/* faq */
.faq{position:absolute;top:1575px;left:0;width:1200px;height:269px;background:var(--dark);color:var(--white)}
.faq .section-title{color:var(--white);position:absolute;top:44px;left:0;width:1200px;justify-content:center}
.faq .section-title .bar{background:var(--white)}
.badge{position:absolute;width:47px;height:47px;border-radius:50%;display:flex;align-items:center;justify-content:center;font-size:26px;font-weight:700}
/* instagram */
.shot{position:absolute;top:1955px;width:155px;height:155px}
/* footer */
.footer{position:absolute;top:2217px;left:0;width:1200px;height:338px;background:var(--light)}
.footer h5{position:absolute;font-size:12.5px;font-weight:600;color:var(--ink)}
.footer .small{position:absolute;font-size:10px;line-height:15px;color:var(--ink);font-weight:500}
.social{position:absolute;top:2491px;width:24px;height:24px;border-radius:50%;border:1px solid var(--orange)}
</style>
</head>
<body>

<!-- header -->
<div class="brand" style="left:200px;top:18px;font-size:20px"><span class="dot"></span>Hearthside Events</div>
<nav class="nav">
  <span class="active">-- Home --</span><span>About Us</span><span>Services</span><span>FAQ</span><span>Contact Us</span>
</nav>
<div class="phone">
  <svg width="9" height="13" viewBox="0 0 9 13"><rect x="1" y="1" width="7" height="11" rx="1.5" fill="none" stroke="#f47216" stroke-width="1.3"/></svg>
  (555) 014-2290
</div>
<div class="btn" style="left:888px;top:19px;width:112px;height:25px">Check Availability</div>

<!-- hero -->
<div class="hero" role="img" aria-label="Photo of the event trailer with covered porch and string lights beside a house"></div>
<div class="hero-copy">
  <h3>Welcome to Hearthside Events</h3>
  <h1>We provide everything you need to<br>host any&nbsp; event desired!!</h1>
</div>
<div class="btn" style="left:550px;top:325px;width:100px;height:24px">Contact Us</div>

<!-- about -->
<section class="about">
  <div class="section-title abs" style="left:200px;top:46px">About us <span class="bar"></span></div>
  <div class="abs" style="left:200px;top:97px;width:530px">
    <p><b style="color:var(--ink)">Welcome to Hearthside Events ! We provide everything you need to host any&nbsp; event desired!!</b><br>Our goal is to provide an atmosphere that will blow away the&nbsp; competition and leave you feeling that you hosted an event which will leave everyone&nbsp; talking!!</p>
    <p style="margin-top:15px">We are event planners who will provide all the goods and bring new ideas to the table&nbsp; that have never been done before! Starting with our main attraction the Hearthside entertainment trailer which was just completed last summer! We typically start booking&nbsp; your event with the entertainment trailer and build off of that. Whatever the occasion&nbsp; and whatever you desire, we will go beyond your expectations!</p>
    <p style="margin-top:15px;color:var(--orange)">[ More ... ]</p>
  </div>
</section>
<div class="frame"></div>
<form class="card">
  <h4>Check Availability</h4>
  <div class="field">Name</div>
  <div class="field">Phone</div>
  <div class="field">Email Address</div>
  <div class="field">Date Request
    <svg width="9" height="9" viewBox="0 0 9 9"><rect x="0.5" y="1.5" width="8" height="7" fill="none" stroke="#f47216"/><line x1="0.5" y1="3.5" x2="8.5" y2="3.5" stroke="#f47216"/></svg>
  </div>
  <div class="submit">Check Availability</div>
</form>

<!-- services -->
<div class="section-title abs" style="left:0;top:873px;width:1200px;justify-content:center"><span class="bar"></span>Services we provide<span class="bar"></span></div>
<div class="abs" style="left:200px;top:934px;width:800px;height:1px;background:var(--line)"></div>
<div class="acc" style="top:935px">Full Entertainment Trailer Rental<span class="plus"></span></div>
<div class="acc" style="top:973px">Table and Chair Packages<span class="plus"></span></div>
<div class="acc" style="top:1011px">Whiskey Barrel Rentals<span class="plus"></span></div>
<div class="acc open" style="top:1049px">Tent Setup Pricing<span class="plus"></span></div>

<div class="abs" style="left:200px;top:1112px;width:388px;height:313px;background:linear-gradient(160deg,#3f5a3a,#8a9488 45%,#a6927a 70%,#3b3a36)" role="img" aria-label="Photo from above of a white tent attached to the trailer with tables and whiskey barrels"></div>
<div class="tent-text">
  <h3>Tent Setup Pricing</h3>
  <p><b>Tents which are connected to the side of the trailer are rented in<br>12 foot sections.</b> Each section extends12 feet out from the side of the trailer and is 25 in length which is the same size as the trailer. Also, each 12 foot section of tent includes 3 whiskey barrels with poles included for tent support. (One for each side and one in the middle to support the tent center height)</p>
  <ul>
    <li><svg width="14" height="12" viewBox="0 0 14 12"><path d="M1 6l4 4 8-9" fill="none" stroke="#f47216" stroke-width="2"/></svg>1- 12 by 25 section of tent and 3 whiskey barrels included priced at <b>$225</b></li>
    <li><svg width="14" height="12" viewBox="0 0 14 12"><path d="M1 6l4 4 8-9" fill="none" stroke="#f47216" stroke-width="2"/></svg>1-24 by 25 foot section of tent includes 6 whiskey barrels for the price of <b>$450</b></li>
    <li><svg width="14" height="12" viewBox="0 0 14 12"><path d="M1 6l4 4 8-9" fill="none" stroke="#f47216" stroke-width="2"/></svg>1- 36 by 25 foot section of tent includes 9 whiskey barrels for the price of <b>$675</b></li>
  </ul>
</div>
<div class="btn" style="left:613px;top:1389px;width:113px;height:24px">Check Availability</div>

<div class="acc" style="top:1450px;border-top:1px solid var(--line)">Lighting Rental and Setup Options<span class="plus"></span></div>
<div class="acc" style="top:1488px">DJs, Bartenders,and Party Hosts<span class="plus"></span></div>

<!-- faq -->
<section class="faq">
  <div class="section-title"><span class="bar"></span>FAQ<span class="bar"></span></div>
  <div class="badge" style="left:200px;top:105px;background:var(--white);color:var(--ink)">Q</div>
  <div class="abs" style="left:281px;top:103px;font-size:22px;font-weight:600;line-height:28px">How does the trailer<br>have lighting and water?</div>
  <div class="badge" style="left:613px;top:105px;background:var(--orange);color:var(--white)">A</div>
  <p class="abs" style="left:690px;top:108px;width:312px;font-size:11px;line-height:15px">During the setup process of the Hearthside entertainment trailer we will connect a black&nbsp; garden hose to the closest connection available and we will run a power cord connection from the trailer to a typical common 110 volt outlet. Most likely these will&nbsp; run across the driveway or an area your guests will be walking so we will include a plastic yellow safety protector for the cord and hose to run through making it safe for&nbsp; guests to walk over</p>
</section>

<!-- instagram -->
<div class="section-title abs" style="left:0;top:1886px;width:1200px;justify-content:center"><span class="bar"></span>@hearthsideevents<span class="bar"></span></div>
<div class="shot" style="left:200px;background:linear-gradient(#e8e4de,#7d6a5a 60%,#3c3c3c)" role="img" aria-label="Trailer porch with steps and flowers"></div>
<div class="shot" style="left:361px;background:linear-gradient(#5c6264,#c88a50 45%,#e9e7e3)" role="img" aria-label="Trailer interior with round tables and chairs"></div>
<div class="shot" style="left:522px;background:linear-gradient(#d9dde2,#9aa1a6 50%,#3e4143)" role="img" aria-label="Tent setup in a driveway in front of a house"></div>
<div class="shot" style="left:683px;background:linear-gradient(#efefef,#8a8f8a 50%,#4a4540)" role="img" aria-label="Under the tent with barrels and stools"></div>
<div class="shot" style="left:844px;background:linear-gradient(#f1f1ef,#9e7a5c 45%,#4d5a3f)" role="img" aria-label="Side view of the trailer porch among trees"></div>
<div class="btn" style="left:531px;top:2143px;width:138px;height:24px">Follow us on Instagram</div>

<!-- footer -->
<footer class="footer"></footer>
<div class="brand" style="left:200px;top:2300px;font-size:19px"><span class="dot"></span>Hearthside Events</div>

<h5 class="abs" style="left:406px;top:2278px;font-size:12.5px;font-weight:600;color:var(--ink)">Contact Us</h5>
<div class="abs" style="left:406px;top:2315px;font-size:12.5px;font-weight:500;color:var(--ink);display:flex;gap:5px;align-items:center">
  <span style="color:var(--orange)">Call Us:</span>
  <svg width="12" height="12" viewBox="0 0 12 12"><path d="M2 1l2.5 0 1 3-1.5 1c.6 1.4 1.6 2.4 3 3l1-1.5 3 1V11c-5 0-9-4-9-9z" fill="none" stroke="#f47216"/></svg>
  +1 555-014-2290
</div>
<div class="abs" style="left:406px;top:2333px;font-size:10px;font-weight:500;color:var(--ink)">hello@hearthsideevents.com</div>
<div class="abs" style="left:406px;top:2366px;font-size:10px;color:var(--orange)">Address:</div>
<div class="abs" style="left:406px;top:2384px;font-size:10px;line-height:15px;font-weight:500;color:var(--ink)">48 Orchard Lane, Millbrook,<br>MA 01742</div>
<div class="btn" style="left:406px;top:2434px;width:113px;height:24px">Check Availability</div>

<h5 class="abs" style="left:612px;top:2278px;font-size:12.5px;font-weight:600;color:var(--ink)">Services We Provide</h5>
<div class="abs" style="left:612px;top:2313px;font-size:10px;line-height:22.5px;font-weight:500;color:var(--ink)">Full Entertainment Trailer Rental<br>Table and Chair Packages<br>Whiskey Barrel Rentals<br>Tent Setup Pricing<br>Lighting Rental and Setup Options<br>DJs, Bartenders,and Party Hosts</div>

<h5 class="abs" style="left:818px;top:2278px;font-size:12.5px;font-weight:600;color:var(--ink)">Subscribe Newsletter</h5>
<div class="abs" style="left:818px;top:2315px;width:182px;height:24px;border-radius:12px;background:#7b7b7b;color:var(--white);font-size:9.5px;display:flex;align-items:center;padding-left:13px">Enter your email ...</div>
<div class="btn" style="left:818px;top:2347px;width:76px;height:24px">Subscribe</div>

<div class="abs" style="left:200px;top:2500px;font-size:9.5px;font-weight:500;color:var(--ink)">© 2021 <span style="color:var(--orange)">Hearthside Events</span>. All Rights Reserved</div>
<div class="social" style="left:613px"></div>
<div class="social" style="left:643px;background:var(--orange)"></div>
<div class="social" style="left:673px"></div>
<svg class="abs" style="left:993px;top:2503px" width="14" height="16" viewBox="0 0 14 16"><path d="M1 15L7 1l6 14M3.5 9.5h7" fill="none" stroke="#f47216" stroke-width="1.5"/></svg>

</body>
</html>
```